Automotive parts Package (box) design

We are developing a new packaging concept for our automotive service and suspension parts line. I will share 2–3 sample designs—some from other brands and some AI‑generated—and we need a designer to create a unified, original design direction based on these references.

We already have an established brand name, VEK, along with a logo. The logo may be updated or redesigned, but the brand name VEK must remain.

- The project includes creating the full packaging design for our product boxes, developing or refining the logo if needed.

-Then, after choosing the design, we will apply the same design to 8 boxes with small customisation for each box to match the product.

- The box die-lines will be provided by us.

Attached are a few sample designs. We need you to develop three or more new designs in a similar style. If you have additional creative concepts beyond these references, you are welcome to include them. The only fixed requirement is that the brand name VEK must remain unchanged in all proposed designs.

Box files such as PNG, PDF (ready-to-print file) and Ai (Editable/ Source file) and fonts with 3D mockup images at the end of the project must be given to us.

Target Market(s)

Car spare parts shops

Industry/Entity Type

Auto Parts

Requirements
Must have
• Our brand name VEK
Nice to have
• Package similar to big auto parts suppliers such as MLP, KRUVE

```html
<!DOCTYPE html>
<html lang="en">
<head>
<meta charset="utf-8">
<title>VEK Service Parts – Box Front Panel</title>
<link rel="stylesheet" href="https://fonts.googleapis.com/css2?family=Archivo+Black&family=Montserrat:wght@600;800&display=swap">
<style>
  :root {
    --page-bg: #ffffff;
    --panel-black: #0b0b0c;
    --panel-charcoal: #1b1b1d;
    --brand-red: #c0191f;
    --deep-red: #8a0508;
    --soft-white: #fbeff0;
    --steel-light: #e4e6e8;
    --steel-mid: #9ea3a8;
    --steel-dark: #4a4e52;
    --line-grey: rgba(255,255,255,0.18);
  }
  * { box-sizing: border-box; margin: 0; padding: 0; }
  html, body { width: 909px; height: 1200px; overflow: hidden; background: var(--page-bg); }
  .canvas { position: relative; width: 909px; height: 1200px; }
  .front-panel {
    position: absolute; left: 43px; top: 371px; width: 824px; height: 458px;
    overflow: hidden;
    background: radial-gradient(ellipse at 40% 55%, var(--panel-charcoal) 0%, var(--panel-black) 70%);
  }
  .panel-graphics { position: absolute; inset: 0; }
  .brand-name {
    position: absolute; left: 57px; top: 54px;
    font-family: "Archivo Black", sans-serif; font-size: 56px; line-height: 1;
    color: var(--brand-red); letter-spacing: 2px;
  }
  .brand-tagline {
    position: absolute; left: 58px; top: 116px;
    font-family: "Montserrat", sans-serif; font-weight: 600; font-size: 12px;
    color: #ffffff; letter-spacing: 0.2px;
  }
  .headline {
    position: absolute; left: 55px; top: 150px;
    font-family: "Archivo Black", sans-serif; font-size: 76px; line-height: 72px;
    letter-spacing: -2px; font-weight: 400;
  }
  .headline-service { display: block; color: var(--soft-white); }
  .headline-parts { display: block; color: var(--brand-red); }
  .headline-rule {
    position: absolute; left: 57px; top: 315px; width: 128px; height: 2px;
    background: var(--brand-red);
  }
  .name-band {
    position: absolute; left: 0; top: 347px; width: 470px; height: 52px;
    background: linear-gradient(90deg, var(--brand-red) 0%, rgba(192,25,31,0.55) 45%, rgba(192,25,31,0) 100%);
  }
  .name-band-text {
    position: absolute; left: 58px; top: 14px;
    font-family: "Montserrat", sans-serif; font-weight: 800; font-size: 18px;
    color: #ffffff; letter-spacing: 0.3px; white-space: nowrap;
  }
  .product-visual {
    position: absolute; left: 454px; top: 96px; width: 236px; height: 218px;
    border-radius: 46% 40% 44% 38%;
    background: radial-gradient(ellipse at 45% 45%, var(--steel-light) 0%, var(--steel-mid) 45%, var(--steel-dark) 80%, rgba(74,78,82,0) 100%);
  }
</style>
</head>
<body>
<main class="canvas">
  <section class="front-panel">
    <svg class="panel-graphics" width="824" height="458" viewBox="0 0 824 458" aria-hidden="true">
      <defs>
        <linearGradient id="red-field" x1="0" y1="1" x2="1" y2="0">
          <stop offset="0" stop-color="#6e0205"/>
          <stop offset="0.5" stop-color="#9a0a0e"/>
          <stop offset="1" stop-color="#7a0306"/>
        </linearGradient>
        <path id="badge-top" d="M 699 355 A 33 33 0 0 1 765 355"/>
        <path id="badge-bottom" d="M 697 355 A 35 35 0 0 0 767 355"/>
      </defs>
      <polygon points="379,458 824,87 824,458" fill="url(#red-field)"/>
      <polygon points="340,458 824,55 824,72 360,458" fill="#050505"/>
      <line x1="305" y1="458" x2="824" y2="25" stroke="var(--line-grey)" stroke-width="1"/>
      <line x1="610" y1="68" x2="824" y2="68" stroke="var(--line-grey)" stroke-width="1"/>
      <line x1="240" y1="170" x2="470" y2="170" stroke="rgba(255,255,255,0.08)" stroke-width="1"/>
      <circle cx="732" cy="355" r="41" fill="none" stroke="#ffffff" stroke-width="1"/>
      <text font-family="Montserrat, sans-serif" font-weight="800" font-size="8" fill="#ffffff" letter-spacing="0.6">
        <textPath href="#badge-top" startOffset="50%" text-anchor="middle">6 MONTH</textPath>
      </text>
      <text font-family="Montserrat, sans-serif" font-weight="800" font-size="8" fill="#ffffff" letter-spacing="0.6" dy="8">
        <textPath href="#badge-bottom" startOffset="50%" text-anchor="middle">WARRANTY</textPath>
      </text>
      <g class="warranty-icon" fill="none" stroke="#ffffff" stroke-width="1.4" stroke-linejoin="round">
        <circle cx="732" cy="347" r="11"/>
        <circle cx="732" cy="347" r="7"/>
        <polyline points="728.5,347 731,349.5 735.5,344.5"/>
        <polyline points="725,356 721,368 726,366 728,370 731,358"/>
        <polyline points="739,356 743,368 738,366 736,370 733,358"/>
      </g>
    </svg>

    <div class="brand-name">VEK</div>
    <div class="brand-tagline">AUTOMOTIVE COMPONENTS</div>

    <h1 class="headline">
      <span class="headline-service">SERVICE</span>
      <span class="headline-parts">PARTS</span>
    </h1>
    <div class="headline-rule"></div>

    <div class="name-band"><span class="name-band-text">VEK AUTOMOTIVE COMPONENTS</span></div>

    <div class="product-visual" role="img" aria-label="Chrome engine pistons, connecting rods and crankshaft assembly"></div>
  </section>
</main>
</body>
</html>
```